Ward Compass Business Card Design*

We need a business card design for our company Ward Compass. Our company is specialized in providing online consulting services regarding medical institutions, hospitals and doctors. We work with patients worldwide looking to choose between healthcare providers. We have a website you may use as a reference, where we list doctors and clinics worldwide. So we target Medical providers as well as patients worldwide.
Target Market(s)
Medical Providers and patients around the world
Industry/Entity Type
Medical
Contact Information for Business Card
Salma Derkaoui
CEO
+90 612 348 2071
info@wardcompass-example.com
www.wardcompass-example.com
14 Annakhil 3 H.R.B. Rabat, Morocco
Requirements
Must have
- Company logo/name on one full side, personal info and smaller logo and company name on the other side.
Nice to have
- Smart and elegant design

```html
<!DOCTYPE html>
<html lang="en">
<head>
<meta charset="utf-8">
<title>Ward Compass – Business Card</title>
<link rel="stylesheet" href="https://fonts.googleapis.com/css2?family=Didact+Gothic&display=swap">
<style>
  :root {
    --page-bg: #e9e9e6;
    --card-white: #ffffff;
    --lime: #a3fc05;
    --navy: #1d1f8a;
    --muted-grey: #b9c2c0;
    --ink-white: #ffffff;
    --card-w: 822px;
    --card-h: 470px;
  }
  * { box-sizing: border-box; margin: 0; padding: 0; }
  html, body {
    width: 1200px; height: 1016px; overflow: hidden;
    background: var(--page-bg);
    font-family: "Didact Gothic", "Century Gothic", sans-serif;
  }
  .card {
    position: absolute; left: 189px;
    width: var(--card-w); height: var(--card-h);
    overflow: hidden;
    box-shadow: 0 4px 14px rgba(0,0,0,.18);
  }
  /* Front side */
  .card-front { top: 25px; background: var(--card-white); }
  .front-top-bar {
    position: absolute; left: 48%; top: 4%;
    width: 29%; height: 7%;
    background: var(--lime);
  }
  .front-holder {
    position: absolute; right: 23%; top: 13.5%;
    text-align: right; color: var(--muted-grey);
  }
  .front-holder .holder-name { font-size: 30px; letter-spacing: 3px; line-height: 1.1; }
  .front-holder .holder-role { font-size: 18px; letter-spacing: 2px; margin-top: 2px; line-height: 1; }
  .front-block {
    position: absolute; left: 61%; top: 64%;
    width: 33%; height: 36%;
    background: var(--lime);
  }
  .front-brand {
    position: absolute; left: 14%; top: 40%;
    display: flex; align-items: center; gap: 22px;
    color: var(--navy);
  }
  .brand-dot {
    width: 104px; height: 104px; border-radius: 50%;
    background: var(--navy); flex: none;
  }
  .front-brand .brand-name { font-size: 58px; letter-spacing: 3px; line-height: 1; }

  /* Back side */
  .card-back { top: 521px; background: var(--lime); color: var(--ink-white); }
  .back-brand {
    position: absolute; left: 0; right: 0; top: 12%;
    display: flex; justify-content: center; align-items: center; gap: 14px;
  }
  .back-brand .brand-dot { width: 56px; height: 56px; background: var(--ink-white); }
  .back-brand .brand-name { font-size: 32px; letter-spacing: 3px; }
  .back-details {
    position: absolute; left: 0; right: 0; top: 39%;
    display: flex; justify-content: center; align-items: stretch;
  }
  .holder {
    text-align: right; padding-right: 26px;
    display: flex; flex-direction: column; justify-content: flex-end;
  }
  .holder .holder-name { font-size: 38px; letter-spacing: 2px; line-height: 1; }
  .holder .holder-role { font-size: 22px; letter-spacing: 2px; }
  .divider { width: 2px; background: var(--ink-white); }
  .contacts { list-style: none; padding-left: 26px; }
  .contacts li {
    display: flex; align-items: center; gap: 16px;
    font-size: 21px; letter-spacing: 1.5px; height: 40px;
  }
  .contacts svg { width: 26px; height: 26px; flex: none; }
  .rule {
    position: absolute; left: 10%; right: 10%; top: 76%;
    height: 2px; background: var(--ink-white);
  }
  .address {
    position: absolute; left: 0; right: 0; top: 81%;
    text-align: center; font-size: 24px; letter-spacing: 2px;
  }
</style>
</head>
<body>
  <section class="card card-front" aria-label="Business card front">
    <div class="front-top-bar"></div>
    <div class="front-holder">
      <p class="holder-name">Salma Derkaoui</p>
      <p class="holder-role">CEO</p>
    </div>
    <div class="front-block"></div>
    <div class="front-brand">
      <span class="brand-dot"></span>
      <span class="brand-name">WARD COMPASS</span>
    </div>
  </section>

  <section class="card card-back" aria-label="Business card back">
    <div class="back-brand">
      <span class="brand-dot"></span>
      <span class="brand-name">WARD COMPASS</span>
    </div>
    <div class="back-details">
      <div class="holder">
        <p class="holder-name">Salma Derkaoui</p>
        <p class="holder-role">CEO</p>
      </div>
      <div class="divider"></div>
      <ul class="contacts">
        <li>
          <svg viewBox="0 0 24 24" aria-hidden="true"><path fill="#fff" d="M4 9c0-3 3-5 8-5s8 2 8 5v2h-4V9H8v2H4z M7 12h10l2 8H5z"/></svg>
          +90 612 348 2071
        </li>
        <li>
          <svg viewBox="0 0 24 24" aria-hidden="true" fill="none" stroke="#fff" stroke-width="1.6"><rect x="2.5" y="5.5" width="19" height="13"/><path d="M2.5 5.5l9.5 8 9.5-8M2.5 18.5l7-6.5M21.5 18.5l-7-6.5"/></svg>
          info@wardcompass-example.com
        </li>
        <li>
          <svg viewBox="0 0 24 24" aria-hidden="true" fill="none" stroke="#fff" stroke-width="1.6"><circle cx="12" cy="12" r="9.5"/><ellipse cx="12" cy="12" rx="4" ry="9.5"/><path d="M2.5 12h19M4 7h16M4 17h16"/></svg>
          www.wardcompass-example.com
        </li>
      </ul>
    </div>
    <div class="rule"></div>
    <p class="address">14 Annakhil 3 H.R.B. Rabat, Morocco</p>
  </section>
</body>
</html>
```